Physical Therapy Center for children Business Card

We need a Business Card for our company (Physical Therapy for children and youth with special needs) in Lisbon, Portugal. The name of the company is "Luz do Caminho"

The card must contain the following info:
- Logo: see uploaded file
- Name: Luz do Caminho
- Slogan: Semeamos Amor, colhemos sorrisos, distribuímos vitórias!
- Service: Terapias Especializadas
- Address: Rua Henrique Valente Morais 4B
- ZipCode: 2719-583 Póvoa de Santa Iria
- E-mail: geral@luzina.pt
- Site: www.luzina.pt
- Facebook: www.facebook.com/luzdocaminho
- Phone: +351 21 547 60 29
- Cell Phone: +351 96 718 45 93

The stationary should have contain all info from business card.

Target Market(s)

Parents of children with special needs

Industry/Entity Type

Physical Therapy

Contact Information for Business Card

The card design should be compatible with http://www.vellotype.com/product2/order_detail.php?gid=40

Requirements
Should not have
• The business card should not have a Black background. Use white or other color.

```html
<!DOCTYPE html>
<html lang="pt">
<head>
<meta charset="utf-8">
<title>Luz do Caminho — Cartão de Visita</title>
<link href="https://fonts.googleapis.com/css2?family=Comfortaa:wght@400;600&family=Arimo:wght@400&display=swap" rel="stylesheet">
<style>
  :root {
    --page-bg: #ecebe8;
    --card-bg: #ffffff;
    --teal: #19a592;
    --ink: #1d1d1d;
    --muted: #555555;
    --shadow: rgba(0, 0, 0, 0.16);
  }
  html, body {
    margin: 0;
    width: 1200px;
    height: 1200px;
    overflow: hidden;
    background: var(--page-bg);
  }
  .card {
    position: absolute;
    left: 100px;
    top: 300px;
    width: 1000px;
    height: 600px;
    background: var(--card-bg);
    box-shadow: 0 12px 40px var(--shadow);
  }
  .brand-mark {
    position: absolute;
    left: 60px;
    top: 250px;
    width: 300px;
    display: flex;
    align-items: center;
    gap: 14px;
    font-family: "Comfortaa", sans-serif;
    font-weight: 600;
    font-size: 30px;
    color: var(--teal);
    white-space: nowrap;
  }
  .brand-mark .dot {
    flex: none;
    width: 22px;
    height: 22px;
    border-radius: 50%;
    background: var(--teal);
  }
  .divider {
    position: absolute;
    left: 395px;
    top: 70px;
    width: 3px;
    height: 460px;
    background: var(--teal);
  }
  .company-name {
    position: absolute;
    left: 440px;
    top: 72px;
    margin: 0;
    font-family: "Comfortaa", sans-serif;
    font-weight: 400;
    font-size: 32px;
    line-height: 40px;
    color: var(--teal);
    letter-spacing: 0.5px;
  }
  .service {
    position: absolute;
    left: 440px;
    top: 128px;
    margin: 0;
    font-family: "Comfortaa", sans-serif;
    font-weight: 400;
    font-size: 20px;
    line-height: 26px;
    color: var(--teal);
  }
  .slogan {
    position: absolute;
    left: 440px;
    top: 166px;
    width: 520px;
    margin: 0;
    font-family: "Arimo", sans-serif;
    font-size: 17px;
    line-height: 22px;
    color: var(--muted);
  }
  .contacts {
    position: absolute;
    left: 440px;
    top: 284px;
    margin: 0;
    padding: 0;
    list-style: none;
    font-family: "Arimo", sans-serif;
    font-size: 21px;
    color: var(--ink);
  }
  .contacts li {
    display: flex;
    align-items: center;
    gap: 18px;
    height: 32px;
    white-space: nowrap;
  }
  .contacts .icon {
    flex: none;
    width: 22px;
    height: 22px;
  }
  .contacts .zip {
    padding-left: 40px;
  }
  .contacts .facebook {
    margin-top: 6px;
    font-size: 22px;
  }
</style>
</head>
<body>
  <section class="card" aria-label="Cartão de visita Luz do Caminho">
    <div class="brand-mark"><span class="dot"></span>Luz do Caminho</div>

    <div class="divider"></div>

    <h1 class="company-name">Luz do Caminho</h1>
    <p class="service">Terapias Especializadas</p>
    <p class="slogan">Semeamos Amor, colhemos sorrisos, distribuímos vitórias!</p>

    <ul class="contacts">
      <li>
        <svg class="icon" viewBox="0 0 22 22" aria-hidden="true">
          <rect width="22" height="22" rx="3" fill="var(--teal)"/>
          <circle cx="11" cy="11" r="6" fill="none" stroke="#fff" stroke-width="1.6"/>
          <ellipse cx="11" cy="11" rx="2.6" ry="6" fill="none" stroke="#fff" stroke-width="1.3"/>
          <line x1="5" y1="11" x2="17" y2="11" stroke="#fff" stroke-width="1.3"/>
        </svg>
        www.luzina.pt
      </li>
      <li>
        <svg class="icon" viewBox="0 0 22 22" aria-hidden="true">
          <rect width="22" height="22" rx="3" fill="var(--teal)"/>
          <rect x="4.5" y="6.5" width="13" height="9" fill="none" stroke="#fff" stroke-width="1.5"/>
          <polyline points="4.5,6.5 11,12 17.5,6.5" fill="none" stroke="#fff" stroke-width="1.5"/>
        </svg>
        geral@luzina.pt
      </li>
      <li>
        <svg class="icon" viewBox="0 0 22 22" aria-hidden="true">
          <rect width="22" height="22" rx="3" fill="var(--teal)"/>
          <rect x="7" y="4" width="8" height="14" rx="1.5" fill="none" stroke="#fff" stroke-width="1.5"/>
          <circle cx="11" cy="15.3" r="0.9" fill="#fff"/>
        </svg>
        +351 96 718 45 93
      </li>
      <li>
        <svg class="icon" viewBox="0 0 22 22" aria-hidden="true">
          <rect width="22" height="22" rx="3" fill="var(--teal)"/>
          <path d="M7 5 L9.5 5 L10.5 8 L9 9.3 Q10.5 12.5 12.7 13 L14 11.5 L17 12.5 L17 15 Q16 17 13.5 16.5 Q6.5 14 5.5 7.5 Q5.5 5.5 7 5 Z" fill="#fff"/>
        </svg>
        +351 21 547 60 29
      </li>
      <li>
        <svg class="icon" viewBox="0 0 22 22" aria-hidden="true">
          <rect width="22" height="22" rx="3" fill="var(--teal)"/>
          <path d="M11 18 Q5.5 11.5 5.5 9 A5.5 5.5 0 0 1 16.5 9 Q16.5 11.5 11 18 Z" fill="#fff"/>
          <circle cx="11" cy="9" r="2" fill="var(--teal)"/>
        </svg>
        Rua Henrique Valente Morais 4B
      </li>
      <li class="zip">2719-583 Póvoa de Santa Iria</li>
      <li class="facebook">Facebook: www.facebook.com/luzdocaminho</li>
    </ul>
  </section>
</body>
</html>
```